Flower delivery business needs sales brochure

I have a courier business that specialises in same-day flower deliveries; I want to make a single page A4 sales brochure (folded to DL) to give to our potential customers.
The company website is petalvanto.com, this will give an idea of who we are and what we do, as well as some graphics and colours that we use.
When opened, the inside A4 space of the brochure will be a pricelist, so the entire page will be an excel table with delivery locations and prices; we will add the prices ourselves later, so ideally the inside will be a background of some sort that won't obstruct text. Maybe light/transparent flowers and a background colour?
The front of the DL brochure should be mostly a title page, so business name, phone number, a graphic?
The first inside page should relate to our service, there's a lot of info on our website that you could use, so same day delivery, 10:30 and 2:30 pick-up times, established over 10 years ago, air-conditioned vans, delivery to 300+ suburbs.
The back page would be contact details and maybe a summary of the key points of the 'about us' section of the website.

Industry/Entity Type

Business

```html
<!DOCTYPE html>
<html lang="en">
<head>
<meta charset="utf-8">
<title>Petal Vanto – Brochure Outside</title>
<link rel="stylesheet" href="https://fonts.googleapis.com/css2?family=Roboto+Condensed:wght@300;400;700&display=swap">
<style>
  :root {
    --page-bg: #d9d9d9;
    --maroon: #5c1507;
    --maroon-deep: #4a1005;
    --gold: #e0952f;
    --gold-soft: #e6a04a;
    --alert-red: #ee2a24;
    --white: #ffffff;
    --fold-line: rgba(0,0,0,0.28);
  }
  * { box-sizing: border-box; margin: 0; padding: 0; }
  html, body { width: 1200px; height: 1200px; overflow: hidden; }
  body {
    background: var(--page-bg);
    font-family: "Roboto Condensed", "Arial Narrow", sans-serif;
    color: var(--gold-soft);
    position: relative;
  }
  .brochure {
    position: absolute;
    left: 30px; top: 198px;
    width: 1140px; height: 805px;
    display: flex;
    background: var(--maroon);
    box-shadow: 0 6px 24px rgba(0,0,0,0.25);
  }
  .panel {
    position: relative;
    width: 380px; height: 100%;
    border-right: 1px solid var(--fold-line);
    overflow: hidden;
    text-align: center;
  }
  .panel:last-child { border-right: none; }
  .panel--about, .panel--cover {
    background: radial-gradient(ellipse at 100% 0%, rgba(214,120,30,0.55), transparent 40%), var(--maroon);
  }
  .panel--cover {
    background: radial-gradient(ellipse at 0% 0%, rgba(214,120,30,0.55), transparent 40%), var(--maroon);
  }
  .about-title {
    margin-top: 52px;
    font-size: 28px; font-weight: 700; color: var(--gold);
  }
  .about-lead {
    font-size: 18px; font-weight: 700; color: var(--gold); line-height: 1.3;
    margin-top: 2px;
  }
  .about-text {
    font-size: 15.5px; font-weight: 300; line-height: 1.3;
    padding: 0 26px; margin-top: 14px;
  }
  .brand {
    display: flex; align-items: center; justify-content: center; gap: 12px;
  }
  .brand__dot {
    width: 50px; height: 50px; border-radius: 50%; background: #e0602f;
  }
  .brand__name {
    font-size: 33px; font-weight: 400; color: var(--white); letter-spacing: 1px;
    text-transform: uppercase;
  }
  .panel--about .brand { margin: 26px 0 18px; }
  .floral-border {
    position: absolute; left: 0; bottom: 0; width: 100%; height: 150px;
    background: linear-gradient(to bottom, rgba(196,96,20,0) 0%, rgba(196,96,20,0.55) 100%);
  }

  .van-art {
    width: 246px; height: 98px; margin: 0 auto;
    border-radius: 0 0 8px 8px;
    background: linear-gradient(90deg, #e87a22 0%, #f2b13a 35%, #f3f3f3 55%, #dedede 100%);
  }
  .service { text-align: left; padding: 0 28px; }
  .section-title {
    font-size: 26px; font-weight: 700; color: var(--gold); margin-top: 14px;
  }
  .highlight {
    font-size: 18px; font-weight: 700; color: var(--alert-red); line-height: 1.3; margin-top: 6px;
  }
  .times { list-style: none; margin-top: 4px; }
  .times li {
    font-size: 15.5px; font-weight: 300; line-height: 1.3;
    position: relative; padding-left: 16px; margin-bottom: 4px;
  }
  .times li::before {
    content: ""; position: absolute; left: 0; top: 7px;
    width: 8px; height: 8px; border-radius: 50%; background: var(--gold-soft);
  }
  .body-text { font-size: 15.5px; font-weight: 300; line-height: 1.3; margin-top: 6px; }
  .body-text--justify { text-align: justify; }
  .section-title--areas { margin-top: 28px; }
  .divider { border: none; border-top: 1px solid rgba(224,149,47,0.4); margin: 26px 0 30px; }
  .contact { text-align: center; }
  .contact__phone {
    display: flex; align-items: center; justify-content: center; gap: 10px;
    font-size: 29px; color: var(--gold);
  }
  .contact__hours { font-size: 19px; font-weight: 700; color: var(--gold); margin-top: 12px; }
  .contact__hours span { border-left: 1px solid var(--gold); margin: 0 4px; }
  .contact__web { font-size: 18px; font-weight: 700; color: var(--gold); margin-top: 8px; }
  .contact__postal { font-size: 13px; font-weight: 300; line-height: 1.6; margin-top: 8px; }

  .panel--cover .brand { margin-top: 296px; }
  .floral-backdrop {
    position: absolute; left: 0; right: 0; bottom: 0; height: 450px;
    background: radial-gradient(ellipse at 60% 35%, rgba(70,10,3,0.55), rgba(70,10,3,0.15) 70%, transparent 100%);
  }
</style>
</head>
<body>
  <main class="brochure">
    <section class="panel panel--about">
      <h1 class="about-title">Petal Vanto Pty Ltd</h1>
      <p class="about-lead">is a courier company that specializes in<br>the delivery of flowers and gifts.</p>
      <p class="about-text">We offer a same day courier service for the florist &amp; gift retail and wholesale market, and deliver to over 300 suburbs throughout the Brisbane Metropolitan region.</p>
      <p class="about-text">We have been in the business for over 10 years, and are very focused on delivering the best customer service possible.</p>
      <div class="brand"><span class="brand__dot"></span><span class="brand__name">Petal Vanto</span></div>
      <p class="about-text">All our air conditioned vans are specially equipped for the delivery of flowers and are presented to your customer by one of our easily recognizable and professional uniformed drivers.</p>
      <p class="about-text">Our team works hard to build good long term relationships with all our customers and we understand how important it is for your flowers to be delivered on time and in excellent condition.</p>
      <p class="about-text">We understand that its not just the gift of flowers, but the emotion that we are transporting!</p>
      <div class="floral-border" role="img" aria-label="Orange daisy flower border along the bottom edge"></div>
    </section>

    <section class="panel panel--service">
      <div class="van-art" role="img" aria-label="Bunch of gerbera flowers beside a white delivery van"></div>
      <div class="service">
        <h2 class="section-title">Pickup &amp; Delivery Times</h2>
        <p class="highlight">Our service offers pick-ups twice a day<br>for those florists whose volume requires it</p>
        <ul class="times">
          <li>A mid-morning pick-up prior to our depot<br>handover at 11:30 noon</li>
          <li>an afternoon pickup prior to our second<br>depot handover at 2:30pm</li>
        </ul>
        <p class="body-text">Most flowers are delivered within 4/5 hours after pick-up. Local (ie within area of pickup location) and timed deliveries are given priority and we can accommodate for special deadlines with prior notice.</p>
        <h2 class="section-title section-title--areas">Delivery Areas</h2>
        <p class="body-text body-text--justify">We work on a system to ensure that your flowers spend the minimum amount of time in transit as possible. As such, we encourage our customers to supply orders for outlying areas (indicated in blue) to be picked up on the afternoon run, provided they can be delivered after 5:00pm. Most special order requirements can be accommodated with prior notice.</p>
        <hr class="divider">
        <div class="contact">
          <p class="contact__phone">
            <svg width="38" height="38" viewBox="0 0 38 38" aria-hidden="true">
              <circle cx="19" cy="19" r="19" fill="#e0952f"/>
              <path d="M13 9c1-1 2.5-.8 3 .4l1.6 3.6c.4.9 0 1.8-.7 2.3l-1.4 1c.9 2.6 2.6 4.6 5 5.8l1.1-1.3c.6-.7 1.6-.9 2.4-.4l3.4 2c1.1.7 1.1 2.2.1 3.1l-1.7 1.6c-1.4 1.3-3.4 1.5-5.1.6C15 24.9 11.2 20.5 10 15c-.4-1.9.2-3.8 1.5-5z" fill="#4a1005"/>
            </svg>
            0400 555 013
          </p>
          <p class="contact__hours">Mon to Fri : 9am-5pm<span></span>Sat : 9am-3pm</p>
          <p class="contact__web">www.petalvanto.com</p>
          <p class="contact__postal">Postal Address<br>PO Box 4821, Riverside DC QLD, 4000</p>
        </div>
      </div>
    </section>

    <section class="panel panel--cover">
      <div class="floral-backdrop" role="img" aria-label="Faint tone-on-tone daisy silhouettes filling the lower cover"></div>
      <div class="brand" style="position:relative"><span class="brand__dot"></span><span class="brand__name">Petal Vanto</span></div>
    </section>
  </main>
</body>
</html>
```